Business Card Design for Vintage Jazz

I am a vintage jazz band leader in New York City. My groups play the music of the 1920s, 1930s and 1940s. My website is marlowpeskin.com for more info on what I do.

I am looking for a two sided business card design that has the look and feel of a really nice business card from the 1930s. I need to convey with the design that my work has that vintage kind of class and style, but also conveys that we are fun and entertaining.

Most importantly it should make a bold staement. If Hollis Varnum had a card, what would it have looked like? I want a card that I feel confident will make an impact and will let people know that my work is te the top that NYC has to offer in vintage jazz..

Note that I have only decided to avoid the "committed payment" option as I have not used this service before. Assuming that I get quality work I will select a design from those presented.

Target Market(s)

people who want to hire my band for events, media, and new fans of the band

Industry/Entity Type

Performing Art

Contact Information for Business Card

Definitely a matte finish, possibly a sort of old style of paper with that brown tint? definitely a thick card.

Requirements
Must have
• FRONT
• My name: Marlow Peskin
• What I do: Bandleader, Guitarist, Vocalist, Songwriter
• Contact Details: marlowpeskin.com marlow@marlowpeskin.com 646-555-0187
• BACK
• My Social Media Links:
• facebook.marlowpeskin.com
• twitter, instagram, linkedin: marlowpeskin
• I'm also including a photo image I would like to use. The photo's background is not needed, and to be honest isn't really desireable. Just looking to use the image of me.
Nice to have
• I'm attaching which could be used as is, omitted from the card, or altered maybe with text going around the outside of the circle or in some other way. It may need some clean up to the edges of the lettering as we only use it for the website thumbnail.
• If there's space I'd like to include the text "join our mailing list for a free song download: freesong.marlowpeskin.com" If not perhaps just "Download a Free Song at: freesong.marlowpeskin.com - something to this end.
Should not have
• anything cartoony. Don't think retro 90s's vision of the swing era, think actual swing era!
• anything modern. Got to look old school
• Try to avoid dark backgrounds. Since we often play in bars and clubs where it is dar, a d
• avoid script fonts.

```html
<!DOCTYPE html>
<html lang="en">
<head>
<meta charset="utf-8">
<title>Marlow Peskin – Business Card</title>
<link rel="stylesheet" href="https://fonts.googleapis.com/css2?family=Old+Standard+TT:wght@400;700&display=swap">
<style>
  :root {
    --page: #e9e9e7;
    --card-light: #d9b574;
    --card-mid: #c99d55;
    --card-dark: #b98a43;
    --frame: #7a5a24;
    --ink: #111008;
    --ring-light: #f3dc94;
    --ring-dark: #b5862d;
    --portrait-teal: #4fc7b0;
    --portrait-deep: #2e9c88;
  }
  * { box-sizing: border-box; margin: 0; padding: 0; }
  html, body {
    width: 1200px; height: 800px; overflow: hidden;
    background: var(--page);
  }
  .card {
    position: absolute;
    left: 100px; top: 114px;
    width: 1000px; height: 572px;
    border-radius: 30px;
    background: linear-gradient(135deg, var(--card-light) 0%, var(--card-mid) 55%, var(--card-dark) 100%);
    font-family: "Old Standard TT", "Century Schoolbook", Georgia, serif;
    color: var(--ink);
  }
  .card__frame {
    position: absolute; inset: 0;
    width: 1000px; height: 572px;
  }
  .portrait {
    position: absolute;
    left: 120px; top: 44px;
    width: 206px; height: 206px;
    border-radius: 50%;
    background: linear-gradient(145deg, var(--ring-light), var(--ring-dark) 60%, var(--ring-light));
    padding: 10px;
    box-shadow: 0 3px 6px rgba(80, 55, 10, 0.35);
  }
  .portrait__photo {
    width: 100%; height: 100%;
    border-radius: 50%;
    background: radial-gradient(circle at 50% 45%, var(--portrait-teal) 0%, var(--portrait-teal) 55%, var(--portrait-deep) 100%);
  }
  .identity {
    position: absolute;
    right: 62px; top: 268px;
    text-align: right;
  }
  .identity__name {
    font-size: 44px; font-weight: 400;
    letter-spacing: 1px;
    margin-right: 82px;
  }
  .identity__role {
    font-size: 25px; font-weight: 400;
    margin-top: 2px;
  }
  .contacts {
    position: absolute;
    left: 46px; right: 50px; bottom: 64px;
    display: flex; justify-content: space-between; align-items: center;
    font-size: 25px;
    white-space: nowrap;
  }
  .contacts__item { display: flex; align-items: center; gap: 4px; }
  .contacts__sep { margin: 0 2px; }
  .contacts__icon { width: 20px; height: 20px; flex: none; }
</style>
</head>
<body>
  <div class="card">
    <svg class="card__frame" viewBox="0 0 1000 572" aria-hidden="true">
      <g fill="none" stroke="var(--frame)">
        <rect x="18" y="18" width="964" height="536" rx="4" stroke-width="2.5"/>
        <rect x="30" y="30" width="940" height="512" stroke-width="1.2"/>
      </g>
    </svg>

    <div class="portrait">
      <div class="portrait__photo" role="img" aria-label="Black and white portrait of the bandleader in a striped-trim blazer tipping a straw boater hat, on a teal backdrop"></div>
    </div>

    <div class="identity">
      <h1 class="identity__name">Marlow Peskin</h1>
      <p class="identity__role">Bandleader, Guitarist, Vocalist, Songwriter</p>
    </div>

    <div class="contacts">
      <span class="contacts__item">
        <svg class="contacts__icon" viewBox="0 0 24 24" aria-hidden="true">
          <rect x="7" y="4" width="10" height="16" rx="5" fill="none" stroke="var(--ink)" stroke-width="1.5"/>
          <line x1="12" y1="4" x2="12" y2="10" stroke="var(--ink)" stroke-width="1.5"/>
        </svg>
        marlowpeskin.com
      </span>
      <span class="contacts__sep">|</span>
      <span class="contacts__item">
        <svg class="contacts__icon" viewBox="0 0 24 24" aria-hidden="true">
          <rect x="3" y="6" width="18" height="12" fill="none" stroke="var(--ink)" stroke-width="1.5"/>
          <path d="M3 6 L12 13 L21 6" fill="none" stroke="var(--ink)" stroke-width="1.5"/>
        </svg>
        marlow@marlowpeskin.com
      </span>
      <span class="contacts__sep">|</span>
      <span class="contacts__item">
        <svg class="contacts__icon" viewBox="0 0 24 24" aria-hidden="true">
          <path d="M3 9 Q12 2 21 9 L18 11 L15 9 L9 9 L6 11 Z" fill="var(--ink)"/>
          <path d="M7 12 H17 L20 20 H4 Z" fill="var(--ink)"/>
          <circle cx="12" cy="16" r="2" fill="var(--card-mid)"/>
        </svg>
        646-555-0187
      </span>
    </div>
  </div>
</body>
</html>
```